Online retailer needs a Quirky yet professionally designed double sided business car

We mainly sell kitchen and home accessories but pretty much anything new and in demand. Have a look at our site and then come up with designs.
Design to be really catching and want people to visit the website.
Final details such as number, director name and email address will be given to the designer of the winning business card.

Www.zapvelbo.com

Ideas out of the norm also welcome!!

Industry/Entity Type

Business

```html
<!DOCTYPE html>
<html lang="en">
<head>
<meta charset="utf-8">
<title>Zapvelbo Business Card</title>
<link rel="stylesheet" href="https://fonts.googleapis.com/css2?family=Oswald:wght@200;400&family=Open+Sans:wght@400&family=Quicksand:wght@500;700&display=swap">
<style>
  :root {
    --orange: #f48533;
    --ink: #111111;
    --text: #333333;
    --edge: #444444;
    --paper: #ffffff;
    --stage: #ffffff;
  }
  * { box-sizing: border-box; margin: 0; padding: 0; }
  html, body {
    width: 1200px;
    height: 1000px;
    overflow: hidden;
    background: var(--stage);
  }
  .canvas {
    position: relative;
    width: 1200px;
    height: 1000px;
    background: var(--stage);
  }
  .card {
    position: absolute;
    top: 345px;
    width: 540px;
    height: 310px;
    background: var(--paper);
    border: 1.5px solid var(--edge);
    overflow: hidden;
  }
  .card--front { left: 40px; }
  .card--back { left: 620px; }

  /* Front side */
  .brand {
    position: absolute;
    left: 0;
    right: 0;
    top: 88px;
    text-align: center;
  }
  .brand__name {
    display: inline-flex;
    align-items: center;
    gap: 12px;
    font-family: "Quicksand", sans-serif;
    font-weight: 700;
    font-size: 54px;
    line-height: 1;
    color: var(--ink);
  }
  .brand__dot {
    width: 22px;
    height: 22px;
    border-radius: 50%;
    background: var(--orange);
  }
  .brand__tagline {
    margin-top: 6px;
    font-family: "Quicksand", sans-serif;
    font-weight: 500;
    font-size: 17px;
    color: var(--orange);
    letter-spacing: 0.5px;
  }
  .web-band {
    position: absolute;
    left: 0;
    right: 0;
    bottom: 0;
    height: 56px;
    background: var(--orange);
    display: flex;
    align-items: center;
    justify-content: center;
    font-family: "Open Sans", sans-serif;
    font-size: 26px;
    color: var(--paper);
    letter-spacing: 7px;
  }

  /* Back side */
  .identity {
    position: absolute;
    left: 16px;
    top: 104px;
    width: 242px;
    text-align: center;
  }
  .identity__name {
    font-family: "Oswald", sans-serif;
    font-weight: 400;
    font-size: 38px;
    line-height: 1.1;
    color: var(--ink);
    white-space: nowrap;
  }
  .identity__role {
    margin-top: 6px;
    font-family: "Oswald", sans-serif;
    font-weight: 200;
    font-size: 32px;
    line-height: 1;
    color: var(--orange);
  }
  .divider {
    position: absolute;
    left: 268px;
    top: 100px;
    width: 3px;
    height: 106px;
    background: var(--orange);
  }
  .contacts {
    position: absolute;
    left: 332px;
    top: 78px;
    list-style: none;
    font-family: "Open Sans", sans-serif;
    font-size: 15.5px;
    color: var(--text);
  }
  .contacts__item {
    display: flex;
    align-items: flex-start;
    gap: 20px;
    line-height: 23px;
    margin-bottom: 12px;
  }
  .contacts__item:last-child { margin-bottom: 0; }
  .contacts__icon {
    flex: 0 0 16px;
    width: 16px;
    height: 16px;
    margin-top: 3px;
  }
</style>
</head>
<body>
<main class="canvas">

  <section class="card card--front" aria-label="Business card front">
    <div class="brand">
      <div class="brand__name"><span>Zapvelbo</span><span class="brand__dot"></span></div>
      <p class="brand__tagline">gadgets for every home</p>
    </div>
    <div class="web-band">www.zapvelbo.com</div>
  </section>

  <section class="card card--back" aria-label="Business card back">
    <div class="identity">
      <h1 class="identity__name">MARLO FENNICK</h1>
      <p class="identity__role">FOUNDER</p>
    </div>
    <div class="divider"></div>
    <ul class="contacts">
      <li class="contacts__item">
        <svg class="contacts__icon" viewBox="0 0 16 16" aria-hidden="true">
          <path d="M3.5 1.5l2.5 0 1 3.5-1.8 1.3c.8 1.8 2 3 3.8 3.8l1.3-1.8 3.5 1v2.5c0 .8-.7 1.5-1.5 1.5C6.8 13.3 2.7 9.2 2 3c0-.8.7-1.5 1.5-1.5z" fill="var(--orange)"/>
        </svg>
        <span>03 9410 2837</span>
      </li>
      <li class="contacts__item">
        <svg class="contacts__icon" viewBox="0 0 16 16" aria-hidden="true">
          <rect x="1.5" y="3.5" width="13" height="9" fill="none" stroke="var(--orange)" stroke-width="1.2"/>
          <path d="M1.5 3.5l6.5 5 6.5-5" fill="none" stroke="var(--orange)" stroke-width="1.2"/>
        </svg>
        <span>info@zapvelbo.com</span>
      </li>
      <li class="contacts__item">
        <svg class="contacts__icon" viewBox="0 0 16 16" aria-hidden="true">
          <path d="M8 1a5 5 0 0 0-5 5c0 3.6 5 9 5 9s5-5.4 5-9a5 5 0 0 0-5-5z" fill="var(--orange)"/>
          <circle cx="8" cy="6" r="2" fill="var(--paper)"/>
        </svg>
        <span>214 Larkmoor rd,<br>elston north, 3170</span>
      </li>
      <li class="contacts__item">
        <svg class="contacts__icon" viewBox="0 0 16 16" aria-hidden="true">
          <circle cx="8" cy="8" r="6" fill="none" stroke="var(--orange)" stroke-width="1.2"/>
          <ellipse cx="8" cy="8" rx="2.6" ry="6" fill="none" stroke="var(--orange)" stroke-width="1"/>
          <path d="M2 8h12M3 5h10M3 11h10" stroke="var(--orange)" stroke-width="1"/>
        </svg>
        <span>www.zapvelbo.com</span>
      </li>
    </ul>
  </section>

</main>
</body>
</html>
```